In Search of a FANTASTIC BUSINESS CARD REFRESH AND REDESIGN

I would like to redesign the current business card for my company.  There is a parent company, Brookfane Care Group, with 2 operating companies - Brookfane Homecare and Brookfane Senior Living.
I will include the current business card design, along with the 3 logos I would like incorporated.  The business card can be two sided.  I'm looking for something clean, professional, and a fresh new look.

Target Market(s)
Hospitals, social workers, insurance agents, family members of seniors
Industry/Entity Type
Healthcare
Contact Information for Business Card
Name, title of person, address, phone number, web address, email address
Look and feel
Each slider illustrates characteristics of the customer's brand and the style your logo design should communicate.

```html
<!DOCTYPE html>
<html lang="en">
<head>
<meta charset="utf-8">
<title>Brookfane Care Group – Business Card</title>
<link rel="stylesheet" href="https://fonts.googleapis.com/css2?family=Lato:wght@400;700;900&family=Libre+Baskerville:ital@1&display=swap">
<style>
  :root {
    --bg: #2b2b2b;
    --card: #ffffff;
    --ink: #111111;
    --teal: #5f9a98;
    --pink: #ef7f86;
  }
  * { box-sizing: border-box; margin: 0; padding: 0; }
  html, body { width: 1200px; height: 875px; overflow: hidden; }
  body {
    background: var(--bg);
    font-family: "Lato", sans-serif;
    color: var(--ink);
    position: relative;
  }
  .card {
    position: absolute;
    top: 282px;
    width: 540px;
    height: 310px;
    background: var(--card);
    border-radius: 22px;
    overflow: hidden;
  }
  .card--front { left: 40px; }
  .card--back { left: 620px; }

  .brand { display: flex; align-items: center; gap: 8px; font-weight: 700; white-space: nowrap; }
  .brand__square { width: 14px; height: 14px; flex: none; }

  .front__main {
    position: absolute; left: 0; right: 0; top: 102px;
    display: flex; flex-direction: column; align-items: center;
  }
  .front__main .brand { font-size: 30px; color: var(--ink); }
  .front__main .brand__square { width: 26px; height: 26px; background: var(--ink); border-radius: 4px; }
  .tagline {
    margin-top: 14px;
    font-family: "Libre Baskerville", serif;
    font-style: italic;
    font-size: 13px;
    line-height: 1.35;
    text-align: center;
  }
  .front__homecare { position: absolute; left: 34px; bottom: 30px; font-size: 15px; color: var(--pink); }
  .front__homecare .brand__square { background: var(--pink); border-radius: 3px; }
  .front__senior { position: absolute; right: 34px; top: 34px; font-size: 15px; color: var(--teal); }
  .front__senior .brand__square { background: var(--teal); border-radius: 3px; }

  .back__decor {
    position: absolute; left: 0; top: 40px; width: 300px; height: 270px;
    background: linear-gradient(160deg, rgba(95,154,152,.35), rgba(239,127,134,.35));
    border-top-right-radius: 140px;
  }
  .person { position: absolute; left: 40px; top: 168px; }
  .person__name { font-weight: 900; font-size: 26px; letter-spacing: .5px; }
  .person__title { font-size: 15px; margin-top: 2px; }

  .back__info {
    position: absolute; right: 30px; top: 34px;
    display: flex; flex-direction: column; align-items: flex-end;
  }
  .back__info .brand { font-size: 20px; color: var(--ink); margin-bottom: 22px; }
  .back__info .brand__square { background: var(--ink); border-radius: 3px; }
  .contact { list-style: none; font-size: 12.5px; line-height: 1.9; text-align: right; }
  .contact li { display: flex; justify-content: flex-end; align-items: center; gap: 7px; }
  .contact .strong { font-weight: 700; }
  .contact svg { width: 11px; height: 11px; fill: var(--ink); flex: none; }
  .contact .icon-gap { width: 11px; flex: none; }
</style>
</head>
<body>

<section class="card card--front">
  <div class="front__senior brand"><span class="brand__square"></span>Brookfane Senior Living</div>
  <div class="front__main">
    <div class="brand"><span class="brand__square"></span>Brookfane Care Group</div>
    <p class="tagline">Care that stays close to home...<br>Every single day.</p>
  </div>
  <div class="front__homecare brand"><span class="brand__square"></span>Brookfane Homecare</div>
</section>

<section class="card card--back">
  <div class="back__decor" role="img" aria-label="Large soft teal-to-pink brand decoration"></div>
  <div class="person">
    <p class="person__name">DANA HOLLIS</p>
    <p class="person__title">President, CEO</p>
  </div>
  <div class="back__info">
    <div class="brand"><span class="brand__square"></span>Brookfane Care Group</div>
    <ul class="contact">
      <li>(808) 555-0142
        <svg viewBox="0 0 12 12"><path d="M2.5 1l2 2.2-1 1.3a7 7 0 0 0 4 4l1.3-1 2.2 2-1.2 1.5C5.5 11 1 6.5 1 2.2z"/></svg></li>
      <li>(808) 555-0178
        <svg viewBox="0 0 12 12"><rect x="3" y="1" width="6" height="3"/><rect x="1" y="4.5" width="10" height="4.5" rx="1"/><rect x="3" y="8" width="6" height="3"/></svg></li>
      <li>Dana@BrookfaneCare.com
        <svg viewBox="0 0 12 12"><path d="M1 2.5h10v7H1z M1 2.5l5 4 5-4" fill="none" stroke="#111" stroke-width="1.3"/></svg></li>
      <li class="strong">www.BrookfaneCare.com
        <svg viewBox="0 0 12 12"><circle cx="6" cy="6" r="4.8" fill="none" stroke="#111" stroke-width="1.3"/><path d="M1.2 6h9.6M6 1.2c-2.5 3-2.5 6.6 0 9.6M6 1.2c2.5 3 2.5 6.6 0 9.6" fill="none" stroke="#111" stroke-width=".9"/></svg></li>
      <li>480 Lanakila Ave, Ste 210
        <svg viewBox="0 0 12 12"><path d="M6 11.5S2 7 2 4.5a4 4 0 0 1 8 0C10 7 6 11.5 6 11.5z"/><circle cx="6" cy="4.5" r="1.4" fill="#fff"/></svg></li>
      <li>Honolulu, HI 96817<span class="icon-gap"></span></li>
    </ul>
  </div>
</section>

</body>
</html>
```